Slide-Banner für Webseite
Zielgruppe
Lettershop Mailings, kuvertierte Mailings, Selfmailer, Postkarten, Adressierung. Druckerei mit Versand
Aufgabenstellung
Auf der Startseite im oben ein Kind ein Banner mit einem Kind zu sehen.
Hierfür hätte ich gerne drei neue Banner:
1. April Angebot: 100 Euro Gutschein (ab 500 Euro bestellwert)
2. Persönlicher Ansprechpartner - Von der Bestellung bis zur Postauflieferung
3. Lettershop - Mailing - Print - Mailings online kalkulieren und direkt bestellen (das Kind muss weg)
http://kurzlnk.de/Xq7TzR

```html
<!DOCTYPE html>
<html lang="de">
<head>
<meta charset="utf-8">
<title>Slide-Banner Lettershop</title>
<link rel="stylesheet" href="https://fonts.googleapis.com/css2?family=Arimo:wght@400;700&family=Open+Sans:wght@600&display=swap">
<style>
  :root {
    --stage: #e0e0e0;
    --panel: #ffffff;
    --ink: #111111;
    --ink-soft: #555555;
    --ink-muted: #8a8a8a;
    --cyan: #1e9be5;
    --magenta: #e2157f;
    --yellow: #ffed00;
    --black: #2a2a2a;
    --shadow: rgba(0,0,0,0.12);
  }
  * { margin: 0; padding: 0; box-sizing: border-box; }
  html, body { width: 1200px; height: 800px; overflow: hidden; }
  body { background: var(--stage); position: relative; font-family: "Arimo", Arial, sans-serif; color: var(--ink); }
  .banner { position: absolute; background: var(--panel); box-shadow: 0 1px 3px var(--shadow); overflow: hidden; }
  .banner > * { position: absolute; }

  /* Banner 1: Osterangebot */
  .banner--offer { left: 128px; top: 137px; width: 838px; height: 146px; }
  .offer-kicker { left: 24px; top: 22px; font-size: 25px; color: var(--cyan); letter-spacing: -0.5px; }
  .offer-headline { left: 23px; top: 58px; font-size: 29px; font-weight: 700; letter-spacing: -0.6px; }
  .offer-headline sup { font-size: 15px; }
  .offer-note { left: 24px; top: 104px; font-size: 16px; color: var(--ink-muted); letter-spacing: -0.3px; }
  .offer-eggs-fade { left: 380px; top: 0; width: 458px; height: 146px;
    background: linear-gradient(90deg, rgba(240,240,240,0) 0%, #f2f2f2 40%, #f7f7f7 100%); }
  .offer-eggs { left: 532px; top: 10px; width: 300px; height: 124px; border-radius: 60px;
    background: linear-gradient(90deg, var(--magenta) 0%, var(--cyan) 35%, var(--black) 65%, var(--yellow) 100%); opacity: .85; }

  /* Banner 2: Lettershop */
  .banner--shop { left: 128px; top: 334px; width: 840px; height: 148px; }
  .shop-headline { left: 22px; top: 22px; font-size: 33px; font-weight: 700; letter-spacing: -0.8px; }
  .shop-text { left: 22px; top: 68px; font-size: 24px; line-height: 30px; color: var(--ink-soft); letter-spacing: -0.7px; }
  .shop-screens { left: 300px; top: 0; width: 540px; height: 148px;
    background: linear-gradient(90deg, rgba(236,236,236,0) 0%, #ececec 30%, #f4f4f4 70%, #e8e8e8 100%); }
  .shop-brand { left: 600px; top: 106px; width: 234px; height: 40px; background: var(--panel);
    display: flex; align-items: center; justify-content: center;
    font-size: 20px; font-weight: 700; color: var(--ink); letter-spacing: -0.4px; }

  /* Banner 3: Ansprechpartner */
  .banner--contact { left: 131px; top: 528px; width: 840px; height: 148px; }
  .contact-headline { left: 22px; top: 26px; font-size: 26px; font-weight: 700; letter-spacing: -0.5px; }
  .contact-text { left: 23px; top: 64px; font-size: 22px; line-height: 30px; color: var(--ink-soft); letter-spacing: -0.6px; }
  .contact-photo { left: 385px; top: 0; width: 185px; height: 148px;
    background: linear-gradient(90deg, rgba(230,236,242,0) 0%, #d9e2ea 30%, #8fb3d6 55%, #e9edf1 100%); }
  .step { width: 115px; height: 115px; border-radius: 50%; top: 16px;
    display: flex; flex-direction: column; align-items: center; justify-content: center; gap: 8px;
    font-family: "Open Sans", Arial, sans-serif; font-weight: 600; font-size: 12px; color: #fff; }
  .step svg { width: 50px; height: 46px; }
  .step--order { left: 507px; background: var(--cyan); }
  .step--produce { left: 609px; background: var(--magenta); }
  .step--deliver { left: 714px; background: var(--yellow); color: var(--ink); }
</style>
</head>
<body>

<section class="banner banner--offer">
  <div class="offer-eggs-fade"></div>
  <p class="offer-kicker">April Osterangebot</p>
  <h2 class="offer-headline">100 Euro Gutschein geschenkt<sup>*</sup></h2>
  <p class="offer-note">*ab 500 Euro bestellwert</p>
  <div class="offer-eggs" role="img" aria-label="Vier Ostereier in Magenta, Cyan, Schwarz und Gelb mit der Aufschrift 100 €"></div>
</section>

<section class="banner banner--shop">
  <div class="shop-screens" role="img" aria-label="Ansicht des Online-Konfigurators für Selfmailer mit Preisübersicht"></div>
  <h2 class="shop-headline">Lettershop - Mailing - Print</h2>
  <p class="shop-text">Mailings einfach online konfigurieren<br>und direkt bestellen</p>
  <div class="shop-brand">Briefwerk-Versand.de</div>
</section>

<section class="banner banner--contact">
  <h2 class="contact-headline">Persönlicher Ansprechpartner:</h2>
  <p class="contact-text">Beratung aus einer Hand von der<br>Bestellung bis zur Auslierferung</p>
  <div class="contact-photo" role="img" aria-label="Foto eines lächelnden Kundenberaters im hellblauen Hemd"></div>

  <div class="step step--order">
    <svg viewBox="0 0 50 46" fill="none" stroke="#fff" stroke-width="1.8">
      <rect x="13" y="2" width="24" height="38"/>
      <line x1="18" y1="16" x2="20" y2="16"/><line x1="23" y1="16" x2="32" y2="16"/>
      <line x1="18" y1="22" x2="20" y2="22"/><line x1="23" y1="22" x2="32" y2="22"/>
      <line x1="18" y1="28" x2="20" y2="28"/><line x1="23" y1="28" x2="32" y2="28"/>
    </svg>
    Bestellung
  </div>
  <div class="step step--produce">
    <svg viewBox="0 0 50 46" fill="none" stroke="#fff" stroke-width="1.8">
      <polyline points="8,4 8,24 42,24 42,4"/>
      <rect x="16" y="2" width="18" height="14"/>
      <line x1="6" y1="30" x2="44" y2="30"/><line x1="6" y1="35" x2="44" y2="35"/><line x1="6" y1="40" x2="44" y2="40"/>
    </svg>
    Herstellung
  </div>
  <div class="step step--deliver">
    <svg viewBox="0 0 50 46" fill="none" stroke="#111" stroke-width="2">
      <rect x="3" y="8" width="27" height="22" rx="2"/>
      <path d="M30 14 h9 l7 8 v8 h-16z"/>
      <circle cx="12" cy="33" r="4" fill="var(--yellow)"/>
      <circle cx="38" cy="33" r="4" fill="var(--yellow)"/>
    </svg>
    Auslieferung
  </div>
</section>

</body>
</html>
```